New Business Card for our Indoor Golf Training Facility

We are looking for designs for a new business card for our indoor golf training facility. Attached is our logo, our logo with our slogan, and here is our elevator pitch (What makes us different from the others) not sure if all the info will fit on one card, maybe you can condense the elevator pitch? here is the info

Elevator Pitch
We work with serious golfers and those that want to be serious golfers…
to make you better, faster, at all phases of the game…
We use the same state-of-the-art technology as professional golfers…
which produces data sets that shows your improvement in real time.
Our facility is available 24/7 to our members, which allows you to improve on your time.

our website: www.brambleteegolf.com

Target Market(s)

Golfers

Font styles to use
Serif
Sans Serif

Colors
ec1f27
f59195
fbd4d5
919191
d3d3d3
1b1b1b

Requirements
Must have
• our logo or our logo with the slogan, elevator pitch (can be condensed or shortened)

```html
<!DOCTYPE html>
<html lang="en">
<head>
<meta charset="utf-8">
<title>Bramble Tee Golf – Business Card</title>
<link rel="stylesheet" href="https://fonts.googleapis.com/css2?family=Arimo:wght@400;700&family=Open+Sans:wght@300;700;800&display=swap">
<style>
  :root {
    --red: #ec1f27;
    --red-soft: #e8403a;
    --pink: #f59195;
    --blush: #fbd4d5;
    --grey: #919191;
    --light-grey: #d3d3d3;
    --ink: #1b1b1b;
    --white: #ffffff;
    --backdrop: #ecebe8;
  }
  * { box-sizing: border-box; margin: 0; padding: 0; }
  html, body {
    width: 1200px; height: 1000px; overflow: hidden;
    background: var(--backdrop);
    font-family: "Open Sans", Arial, sans-serif;
  }
  .canvas { position: relative; width: 1200px; height: 1000px; }

  .card { position: absolute; box-shadow: 0 10px 30px rgba(0,0,0,.18); }

  /* Front */
  .card-front {
    left: 60px; top: 340px; width: 580px; height: 330px;
    background: linear-gradient(135deg, #f0524a 0%, var(--red-soft) 45%, var(--red) 100%);
    color: var(--white);
    overflow: hidden;
  }
  .front-ring {
    position: absolute; left: 170px; top: 40px; width: 250px; height: 250px;
    border-radius: 50%; border: 26px solid rgba(180,20,20,.18);
  }
  .brand-lockup {
    position: absolute; left: 48px; top: 128px;
    display: flex; align-items: center; gap: 16px;
  }
  .brand-dot {
    width: 56px; height: 56px; border-radius: 50%;
    border: 4px solid var(--white); flex: none;
  }
  .brand-name { font-weight: 800; font-size: 42px; line-height: 1; letter-spacing: -.5px; }
  .brand-slogan {
    position: absolute; left: 122px; top: 182px;
    font-weight: 300; font-size: 19px; letter-spacing: .2px;
  }

  /* Back */
  .card-back {
    left: 700px; top: 180px; width: 400px; height: 640px;
    background: var(--red-soft); padding: 16px;
  }
  .back-panel {
    position: relative; width: 100%; height: 100%;
    background: var(--white); color: var(--ink);
    text-align: center; padding: 76px 8px 0;
    overflow: hidden;
    font-family: "Arimo", Arial, sans-serif;
  }
  .back-ring {
    position: absolute; left: 50%; top: 250px; width: 190px; height: 190px;
    margin-left: -95px; border-radius: 50%;
    border: 10px solid var(--blush); opacity: .8;
  }
  .pitch-title { position: relative; font-weight: 700; font-size: 22px; margin-bottom: 26px; }
  .pitch-line {
    position: relative; font-weight: 700; font-size: 15px; line-height: 1.35;
    margin-bottom: 22px; white-space: nowrap;
  }
  .site-label { position: relative; font-weight: 700; font-size: 15px; margin-top: 4px; }
  .site-url { position: relative; font-weight: 700; font-size: 19px; color: var(--red); }
  .site-url .site-name { color: var(--ink); }
</style>
</head>
<body>
<main class="canvas">
  <section class="card card-front" aria-label="Business card front">
    <div class="front-ring" aria-hidden="true"></div>
    <div class="brand-lockup">
      <span class="brand-dot" aria-hidden="true"></span>
      <span class="brand-name">Bramble Tee Golf</span>
    </div>
    <p class="brand-slogan">Train Smart. Play Sharp. Go Lower.</p>
  </section>

  <section class="card card-back" aria-label="Business card back">
    <div class="back-panel">
      <div class="back-ring" aria-hidden="true"></div>
      <h1 class="pitch-title">Elevator Pitch</h1>
      <p class="pitch-line">We work with serious golfers and those<br>that want to be serious golfers…</p>
      <p class="pitch-line">to make you better, faster,<br>at all phases of the game…</p>
      <p class="pitch-line">We use the same state-of-the-art<br>technology as professional golfers…</p>
      <p class="pitch-line">which produces data sets that shows<br>your improvement in real time.</p>
      <p class="pitch-line">Our facility is available 24/7 to our members<br>which allows you to improve on your time.</p>
      <p class="site-label">our website:</p>
      <p class="site-url">www.<span class="site-name">brambleteegolf</span>.com</p>
    </div>
  </section>
</main>
</body>
</html>
```